Property Management Company

We are looking for a sharp/modern business card design for a property management company.
We have included what should be on the business card down below in business card details.
Target Market(s)
Commercial properties, Home Owners
Industry/Entity Type
Business
Contact Information for Business Card
Name: Dale Orsino | Owner
Business Name : Kestrel Yards
Slogan : A Smarter Choice
Phone : 555.304.8862
Website: www.kestrelyards.example
E-Mail : dale@kestrelyards.example
Our Services are Commercial & Residential
-Asphalt Maintenance
-Snow Management
-Landscaping
-Blacktop
Free Estimates
Free parking lot cleanup & restripe with snow removal contract
Look and feel

```html
<!DOCTYPE html>
<html lang="en">
<head>
<meta charset="utf-8">
<title>Kestrel Yards – Business Card</title>
<link href="https://fonts.googleapis.com/css2?family=Source+Sans+3:wght@400;600;800&display=swap" rel="stylesheet">
<style>
  :root {
    --backdrop: #3b3531;
    --card: #1c1c1d;
    --card-edge: #2a2a2b;
    --white: #f4f4f4;
    --grey: #b9b9b9;
    --red: #d2232e;
    --green: #1f8a3f;
    --rule: #4a4a4a;
  }
  * { box-sizing: border-box; margin: 0; padding: 0; }
  html, body { width: 1200px; height: 844px; overflow: hidden; }
  body {
    background: var(--backdrop);
    font-family: "Source Sans 3", "Myriad Pro", sans-serif;
    position: relative;
  }
  .card {
    position: absolute;
    top: 267px;
    width: 540px;
    height: 310px;
    background: linear-gradient(160deg, var(--card-edge), var(--card) 55%);
    border-radius: 4px;
    box-shadow: 0 12px 30px rgba(0,0,0,.45);
    color: var(--white);
  }
  .card--front { left: 45px; }
  .card--back { left: 615px; }

  .lockup { position: absolute; display: flex; flex-direction: column; }
  .brand {
    display: flex;
    align-items: center;
    gap: 10px;
    font-weight: 800;
    font-size: 30px;
    letter-spacing: .5px;
    text-transform: uppercase;
    line-height: 1;
  }
  .brand__mark { width: 18px; height: 18px; }
  .slogan {
    font-size: 16px;
    font-weight: 600;
    margin-top: 6px;
    line-height: 1;
  }

  .card--front .lockup {
    top: 46px; left: 0; right: 0;
    align-items: center;
  }
  .card--front .brand { color: var(--white); }
  .card--front .brand__mark { background: var(--red); }
  .card--front .slogan { color: var(--green); padding-left: 28px; }

  .person {
    position: absolute;
    top: 160px; left: 30px;
    width: 232px;
    text-align: right;
  }
  .person__name { color: var(--red); font-size: 27px; font-weight: 400; line-height: 1.1; }
  .person__role { color: var(--green); font-size: 18px; line-height: 1.2; margin-bottom: 14px; }
  .person__address { font-size: 18px; line-height: 1.25; }

  .divider {
    position: absolute;
    left: 280px; top: 160px;
    width: 1px; height: 125px;
    background: var(--rule);
  }

  .contacts {
    position: absolute;
    top: 168px; left: 298px;
    list-style: none;
  }
  .contacts li {
    display: flex; align-items: center; gap: 10px;
    font-size: 17px; line-height: 1;
    margin-bottom: 16px;
  }
  .contacts .icon {
    width: 20px; height: 20px;
    background: var(--red);
    border-radius: 2px;
    display: flex; align-items: center; justify-content: center;
    flex: none;
  }
  .contacts svg { width: 13px; height: 13px; }

  .card--back .lockup { top: 128px; left: 42px; }
  .card--back .brand { color: var(--grey); font-size: 29px; }
  .card--back .brand__mark { background: var(--grey); }
  .card--back .slogan { color: var(--white); padding-left: 28px; }

  .services {
    position: absolute;
    top: 52px; left: 312px;
    list-style: none;
    font-size: 16.5px;
    line-height: 20px;
  }
</style>
</head>
<body>

<section class="card card--front" aria-label="Business card front">
  <div class="lockup">
    <div class="brand"><span class="brand__mark"></span>Kestrel Yards</div>
    <p class="slogan">A Smarter Choice</p>
  </div>

  <div class="person">
    <p class="person__name">Dale Orsino</p>
    <p class="person__role">Owner</p>
    <p class="person__address">12345, Address Goes Here<br>Country Name, 123456</p>
  </div>

  <div class="divider"></div>

  <ul class="contacts">
    <li><span class="icon"><svg viewBox="0 0 24 24" fill="#fff"><path d="M6.6 10.8a15.1 15.1 0 0 0 6.6 6.6l2.2-2.2c.3-.3.7-.4 1-.2 1.1.4 2.3.6 3.6.6.6 0 1 .4 1 1V20c0 .6-.4 1-1 1A17 17 0 0 1 3 4c0-.6.4-1 1-1h3.5c.6 0 1 .4 1 1 0 1.3.2 2.5.6 3.6.1.3 0 .7-.2 1z"/></svg></span>555.304.8862</li>
    <li><span class="icon"><svg viewBox="0 0 24 24" fill="#fff"><path d="M3 5h18v14H3zm2 2v.5l7 5 7-5V7z"/></svg></span>dale@kestrelyards.example</li>
    <li><span class="icon"><svg viewBox="0 0 24 24" fill="none" stroke="#fff" stroke-width="2.5" stroke-linecap="round"><path d="M10 14a4 4 0 0 0 5.7 0l3-3a4 4 0 0 0-5.7-5.7l-1 1"/><path d="M14 10a4 4 0 0 0-5.7 0l-3 3a4 4 0 0 0 5.7 5.7l1-1"/></svg></span>www.kestrelyards.example</li>
  </ul>
</section>

<section class="card card--back" aria-label="Business card back">
  <div class="lockup">
    <div class="brand"><span class="brand__mark"></span>Kestrel Yards</div>
    <p class="slogan">A Smarter Choice</p>
  </div>

  <ul class="services">
    <li>Commercial &amp; Residential</li>
    <li>Asphalt Maintenance</li>
    <li>Snow Management</li>
    <li>Landscaping</li>
    <li>Blacktop</li>
    <li>Free Estimates</li>
    <li>Free parking</li>
    <li>Lot cleanup &amp;</li>
    <li>Restripe with</li>
    <li>snow removal contract</li>
  </ul>
</section>

</body>
</html>
```